Veltrix4 Business Card - Health

Veltrix4 maximizes value from the health data of its clients, including doctors, HMOs, and patients. I have attached the Veltrix4 logo as an ai and eps file.
Target Market(s)
Health, HMO, Healthcare, Data, Big Data, Data Analytics
Industry/Entity Type
Business
Requirements
Must have
- At least one side should have some white on it so that we can write on it.

```html
<!DOCTYPE html>
<html lang="en">
<head>
<meta charset="utf-8">
<title>Veltrix4 Business Card</title>
<link href="https://fonts.googleapis.com/css2?family=Jost:wght@400;500&display=swap" rel="stylesheet">
<style>
  :root {
    --page-bg: #d9d6d1;
    --card-bg: #f1f2f3;
    --card-edge: #c9cbcd;
    --ink: #1b1b1b;
    --brand-blue: #1d4fa6;
    --mark-blue: #1f5cc4;
    --title-blue: #2f6cc4;
    --icon-blue: #1f4fa3;
  }
  * { box-sizing: border-box; margin: 0; padding: 0; }
  html, body {
    width: 1200px;
    height: 969px;
    overflow: hidden;
    background: var(--page-bg);
    font-family: "Jost", "Futura", sans-serif;
  }
  .card {
    position: absolute;
    left: 100px;
    top: 201px;
    width: 1000px;
    height: 566px;
    background: var(--card-bg);
    border: 2px solid var(--card-edge);
    box-shadow: 0 20px 50px rgba(0,0,0,0.18);
    overflow: hidden;
  }
  .brand-mark {
    position: absolute;
    left: 28px;
    top: 22px;
    width: 526px;
    height: 526px;
    border-radius: 50%;
    background: var(--mark-blue);
  }
  .brand-name {
    position: absolute;
    right: 53px;
    top: 42px;
    font-size: 84px;
    font-weight: 400;
    letter-spacing: -1px;
    color: var(--ink);
    line-height: 1;
  }
  .accent-bar {
    position: absolute;
    right: 4px;
    top: 173px;
    width: 14px;
    height: 78px;
    background: var(--ink);
  }
  .person-name {
    position: absolute;
    right: 53px;
    top: 172px;
    font-size: 40px;
    font-weight: 500;
    color: var(--brand-blue);
    line-height: 1;
  }
  .person-role {
    position: absolute;
    right: 53px;
    top: 218px;
    font-size: 31px;
    color: var(--title-blue);
    line-height: 1;
  }
  .address {
    position: absolute;
    right: 53px;
    top: 280px;
    text-align: right;
    font-size: 25px;
    line-height: 28px;
    font-style: normal;
    color: var(--ink);
  }
  .contact-list {
    position: absolute;
    right: 46px;
    top: 346px;
    list-style: none;
  }
  .contact-item {
    display: flex;
    justify-content: flex-end;
    align-items: center;
    gap: 14px;
    height: 38px;
    font-size: 25px;
    color: var(--ink);
  }
  .contact-icon {
    width: 26px;
    height: 26px;
    fill: var(--icon-blue);
    flex: none;
  }
</style>
</head>
<body>
  <section class="card" aria-label="Veltrix4 business card">
    <div class="brand-mark" role="img" aria-label="Veltrix4 brand mark area"></div>
    <h1 class="brand-name">Veltrix4</h1>
    <div class="accent-bar"></div>
    <p class="person-name">Marin Holt</p>
    <p class="person-role">CEO/Founder</p>
    <address class="address">
      214 Cedar Hollow Road<br>
      Juneau, Alaska 99801
    </address>
    <ul class="contact-list">
      <li class="contact-item">
        <span>555 210 4817</span>
        <svg class="contact-icon" viewBox="0 0 24 24" aria-hidden="true"><path d="M6.6 10.8a15.1 15.1 0 0 0 6.6 6.6l2.2-2.2c.3-.3.7-.4 1-.2 1.1.4 2.3.6 3.6.6.6 0 1 .4 1 1V20c0 .6-.4 1-1 1C10.6 21 3 13.4 3 4c0-.6.4-1 1-1h3.5c.6 0 1 .4 1 1 0 1.3.2 2.5.6 3.6.1.3 0 .7-.2 1z"/></svg>
      </li>
      <li class="contact-item">
        <span>555 374 9026</span>
        <svg class="contact-icon" viewBox="0 0 24 24" aria-hidden="true"><path d="M7 1h10a2 2 0 0 1 2 2v18a2 2 0 0 1-2 2H7a2 2 0 0 1-2-2V3a2 2 0 0 1 2-2zm0 3v14h10V4zm5 15.2a1.2 1.2 0 1 0 0 2.4 1.2 1.2 0 0 0 0-2.4z"/></svg>
      </li>
      <li class="contact-item">
        <span>555 683 1152</span>
        <svg class="contact-icon" viewBox="0 0 24 24" aria-hidden="true"><path d="M6 2h12v6H6zM3 9h18a1 1 0 0 1 1 1v7h-4v-3H6v3H2v-7a1 1 0 0 1 1-1zm4 6h10v7H7z"/></svg>
      </li>
      <li class="contact-item">
        <span>hello@veltrix4.com</span>
        <svg class="contact-icon" viewBox="0 0 24 24" aria-hidden="true"><path d="M2 5h20v2l-10 6L2 7zm0 4.3l10 6 10-6V19H2z"/></svg>
      </li>
      <li class="contact-item">
        <span>www.veltrix4.com</span>
        <svg class="contact-icon" viewBox="0 0 24 24" aria-hidden="true"><path d="M12 2a10 10 0 1 0 0 20 10 10 0 0 0 0-20zm-1 17.9A8 8 0 0 1 4.1 11H8c.1 3.3 1.2 6.5 3 8.9zm0-8.9H10c.1-2.6.9-5 2-6.9 1.1 1.9 1.9 4.3 2 6.9zm2 8.9c1.8-2.4 2.9-5.6 3-8.9h3.9a8 8 0 0 1-6.9 8.9zM16 9c-.1-2.6-.8-5-2-6.8A8 8 0 0 1 19.9 9z"/></svg>
      </li>
    </ul>
  </section>
</body>
</html>
```